Business Card Design

Need a card designed to fit the tax preparation and accounting profession. Would like to include the following on side two of the card:

Tax Preparation and Audit Representation for:
Individuals
Partnerships
Corporations
Estates
Trusts
Other entities with tax reporting requirements

Industry/Entity Type

Accounting

Contact Information for Business Card

Whitcombe & Associates
Tax and Business Services
Gerald R Whitcombe III, EA, MS
Enrolled Agent P08637519
4172 Marrowind Lane, Suite K
Fernmoor, CA 90000
(555) 482-6157
Email: ledgerpro729@mailbrook.example
www.ledgerhelpdesk.example

```html
<!DOCTYPE html>
<html lang="en">
<head>
<meta charset="utf-8">
<title>Whitcombe &amp; Associates – Business Card</title>
<link rel="stylesheet" href="https://fonts.googleapis.com/css2?family=Libre+Baskerville:wght@400;700&family=Oswald:wght@400&display=swap">
<style>
  :root {
    --red: #c8202a;
    --black: #111214;
    --charcoal: #2a2b2e;
    --white: #ffffff;
    --ink: #1c1c1c;
    --backdrop: #e9e6e1;
    --photo-light: #7d6a5e;
    --photo-dark: #2b2b2e;
  }
  * { box-sizing: border-box; margin: 0; padding: 0; }
  html, body { width: 1200px; height: 784px; overflow: hidden; }
  body {
    background: var(--backdrop);
    font-family: "Libre Baskerville", Georgia, serif;
    position: relative;
  }
  .card {
    position: absolute;
    top: 237px;
    width: 540px;
    height: 309px;
    overflow: hidden;
    box-shadow: 0 6px 18px rgba(0,0,0,0.18);
  }

  /* Back side */
  .card--back {
    left: 40px;
    background: radial-gradient(ellipse at 40% 30%, var(--charcoal) 0%, var(--black) 75%);
    color: var(--white);
    text-align: center;
    padding-top: 40px;
  }
  .services__heading {
    color: var(--red);
    font-size: 15px;
    margin-bottom: 8px;
  }
  .services__list { list-style: none; font-size: 15px; line-height: 28px; }
  .services__other { font-size: 16px; margin-top: 6px; }

  /* Front side */
  .card--front { left: 620px; background: var(--white); }
  .brand-mark {
    position: absolute; left: 30px; top: 34px;
    width: 64px; height: 64px; background: var(--red);
  }
  .brand { position: absolute; left: 112px; top: 30px; }
  .brand__name {
    font-size: 25px; font-weight: 700; color: var(--ink); white-space: nowrap;
  }
  .brand__rule { height: 2px; background: var(--red); width: 296px; margin: 6px 0 5px; }
  .brand__tagline {
    font-family: "Oswald", Arial, sans-serif;
    font-size: 11px; letter-spacing: 4.2px; color: var(--ink);
  }
  .portrait {
    position: absolute; right: 16px; top: 96px;
    width: 110px; height: 146px;
    background: linear-gradient(180deg, var(--photo-light) 0%, var(--photo-dark) 70%);
  }
  .band-rule {
    position: absolute; left: 0; right: 0; top: 242px; height: 3px; background: var(--red);
  }
  .band {
    position: absolute; left: 0; right: 0; top: 248px; bottom: 0; background: var(--black);
  }
  .contact { position: absolute; left: 34px; top: 110px; color: var(--ink); }
  .contact__name { color: var(--red); font-size: 16px; white-space: nowrap; }
  .contact__title { font-size: 12.5px; margin-bottom: 6px; }
  .contact__id { font-size: 12px; margin-bottom: 2px; }
  .contact__list { list-style: none; font-size: 12px; line-height: 18px; }
  .contact__list li { display: flex; align-items: center; gap: 7px; white-space: nowrap; }
  .icon { width: 12px; height: 12px; fill: var(--red); flex: none; }
</style>
</head>
<body>

<section class="card card--back" aria-label="Card back – services">
  <p class="services__heading">Tax Preparation and Audit Representation for</p>
  <ul class="services__list">
    <li>Individuals</li>
    <li>Partnerships</li>
    <li>Corporations</li>
    <li>Estates</li>
    <li>Trusts</li>
  </ul>
  <p class="services__other">Other entities with tax reporting requirements</p>
</section>

<section class="card card--front" aria-label="Card front – contact">
  <div class="brand-mark"></div>
  <div class="brand">
    <p class="brand__name">Whitcombe &amp; Associates</p>
    <div class="brand__rule"></div>
    <p class="brand__tagline">TAX AND BUSINESS SERVICES</p>
  </div>

  <div class="portrait" role="img" aria-label="Portrait photo of the enrolled agent"></div>
  <div class="band-rule"></div>
  <div class="band"></div>

  <div class="contact">
    <p class="contact__name">Gerald R Whitcombe III, EA, MS</p>
    <p class="contact__title">Enrolled Agent</p>
    <p class="contact__id">P08637519</p>
    <ul class="contact__list">
      <li>
        <svg class="icon" viewBox="0 0 24 24" aria-hidden="true"><path d="M6.6 10.8a15.1 15.1 0 0 0 6.6 6.6l2.2-2.2c.3-.3.7-.4 1-.2 1.1.4 2.3.6 3.6.6.6 0 1 .4 1 1V20c0 .6-.4 1-1 1A17 17 0 0 1 3 4c0-.6.4-1 1-1h3.5c.6 0 1 .4 1 1 0 1.3.2 2.5.6 3.6.1.3 0 .7-.2 1z"/></svg>
        (555) 482-6157
      </li>
      <li>
        <svg class="icon" viewBox="0 0 24 24" aria-hidden="true"><path d="M2 5h20v14H2z M4 7v.5l8 5 8-5V7l-8 5z" fill-rule="evenodd"/></svg>
        ledgerpro729@mailbrook.example
      </li>
      <li>
        <svg class="icon" viewBox="0 0 24 24" aria-hidden="true"><circle cx="12" cy="12" r="9" fill="none" stroke="var(--red)" stroke-width="2"/><ellipse cx="12" cy="12" rx="4" ry="9" fill="none" stroke="var(--red)" stroke-width="1.6"/><path d="M3 12h18" stroke="var(--red)" stroke-width="1.6"/></svg>
        www.ledgerhelpdesk.example
      </li>
      <li>
        <svg class="icon" viewBox="0 0 24 24" aria-hidden="true"><path d="M12 3 2 12h3v9h5v-6h4v6h5v-9h3z"/></svg>
        4172 Marrowind Lane, Suite K Fernmoor, CA 90000
      </li>
    </ul>
  </div>
</section>

</body>
</html>
```